依頼詳細
キャンプ場の詳細ホームページがなく、今回新規でホームページを作ることとなりました。
雄大な自然の広がるキャンプ場です。非日常を体験してもらいたいたいです。
川の流れ、きじ、サギ、川鵜、トビ、カッコウ、鴨、ひばり、うぐいすなどの鳥、たぬき、きつね、いたち、いのししの動物も生息しています。

癒やされ、行ってみたくなるようなデザインをお願いします。
サイトURL
http://www.kawabe-leisure-garden.co.jp/resort.html
ページ数
1ページ
希望イメージ
シンプル 複雑
単色 カラフル
暗い 明るい
日常 高級
遊び心 厳粛
未来的 伝統的
女性的 男性的
希望する色
茶系、緑系、アースカラー
納品ファイル
• 高解像度JPG (.jpg)
• イラストレーター形式 (.ai)
• フォトショップ形式 (.psd)
補足説明
レスポンシブデザインを中心にご提案をお願いいたします。
イメージ写真 https://files.example-share.jp/open?id=7kQm2XpR9vTnWcz4Hs81LdEaYb3FuJo5&authuser=hiroaki@orangeleaf.co.jp

イメージ写真等は、有料素材写真等から選定して頂きご提案いただけると大変助かります。

添付写真は必ず使用してほしいものではありません。

```html
<!DOCTYPE html>
<html lang="ja">
<head>
<meta charset="utf-8">
<title>かわべリゾート</title>
<link rel="stylesheet" href="https://fonts.googleapis.com/css2?family=Noto+Sans+JP:wght@400;500;700&family=M+PLUS+Rounded+1c:wght@700;800&display=swap">
<style>
:root{
  --green:#5a9e2f;
  --green-dark:#3f7d1f;
  --leaf:#8cc152;
  --brown:#5a3e28;
  --beige:#f5f0e6;
  --text:#3a3a3a;
  --muted:#777;
  --blue:#1b86cf;
  --orange:#f08c00;
  --white:#fff;
}
*{margin:0;padding:0;box-sizing:border-box}
html,body{width:1200px;height:3324px;overflow:hidden;background:var(--white)}
body{position:relative;font-family:"Noto Sans JP",sans-serif;color:var(--text);font-size:13px;line-height:1.9}
.abs{position:absolute}
.ph{position:absolute;display:block}
.brand{font-family:"Noto Sans JP",sans-serif;font-weight:700;color:var(--green-dark);display:flex;align-items:center;gap:8px}
.brand i{display:inline-block;width:18px;height:18px;border-radius:50%;background:var(--leaf)}
/* header */
.site-header{position:absolute;left:0;top:0;width:1200px;height:44px;background:var(--white);display:flex;align-items:center;padding:0 30px;z-index:3;box-shadow:0 1px 4px rgba(0,0,0,.08)}
.site-header .brand{font-size:17px}
.gnav{display:flex;gap:22px;margin-left:40px;font-size:12px;color:var(--text)}
.reserve-tab{position:absolute;right:0;top:0;width:36px;height:190px;background:var(--orange);color:#fff;writing-mode:vertical-rl;font-size:12px;font-weight:700;display:flex;align-items:center;justify-content:center;letter-spacing:2px;z-index:4}
/* hero */
.hero-title{position:absolute;left:0;width:1200px;top:60px;text-align:center;font-family:"M PLUS Rounded 1c",sans-serif;font-weight:800;font-size:44px;line-height:1.35;color:#fff;text-shadow:0 2px 6px rgba(0,0,0,.45)}
.hero-title span{color:#fff35c}
/* headings */
.sec-title{font-family:"M PLUS Rounded 1c",sans-serif;font-weight:800;color:var(--brown);font-size:26px;text-align:center}
.sec-title.underline{padding-bottom:8px;border-bottom:3px solid var(--leaf);display:inline-block}
.card-title{font-family:"M PLUS Rounded 1c",sans-serif;font-weight:800;color:var(--brown);font-size:24px;margin-bottom:14px}
.body-text{font-size:12px;color:var(--text);line-height:2}
.more-btn{display:inline-flex;align-items:center;gap:8px;margin-top:20px;padding:8px 26px;border:1px solid var(--green);border-radius:20px;font-size:12px;color:var(--green-dark);background:#fff}
.more-btn svg{width:14px;height:14px}
.panel{position:absolute;background:var(--beige);padding:40px 34px}
/* voice */
.voice{position:absolute;width:400px;height:170px;display:flex;gap:18px}
.voice .ph{position:relative;width:170px;height:140px;flex:none}
.voice-body{flex:1 1 auto;min-width:0;overflow-wrap:anywhere}
.voice h4{font-size:15px;color:var(--brown);margin-bottom:6px}
/* faq */
.faq-item{position:absolute;left:150px;width:900px;background:#fff;border-radius:6px;padding:22px 30px 22px 90px;box-shadow:0 2px 8px rgba(0,0,0,.12)}
.faq-item .q{position:absolute;left:26px;top:20px;width:42px;height:42px;border-radius:50%;background:var(--leaf);color:#fff;font-weight:700;font-size:20px;display:flex;align-items:center;justify-content:center}
.faq-item h4{color:var(--green-dark);font-size:16px;margin-bottom:8px}
/* footer */
.site-footer{position:absolute;left:0;top:3030px;width:1200px;height:294px;background:#fff;text-align:center}
.tel-btn{display:inline-block;margin-top:12px;background:var(--green);color:#fff;font-weight:700;font-size:22px;padding:6px 34px;border-radius:4px}
.fnav{display:flex;justify-content:center;gap:26px;font-size:12px;background:#3d3d3d;color:#fff;height:40px;align-items:center}
.copy{font-size:11px;color:var(--muted);margin-top:14px}
</style>
</head>
<body>

<header class="site-header">
  <div class="brand"><i></i>かわべリゾート</div>
  <nav class="gnav"><span>HOME</span><span>施設紹介</span><span>予約の流れ</span><span>よくある質問</span><span>お客様の声</span><span>アクセス</span><span>採用情報</span><span>お問い合わせ</span></nav>
</header>
<div class="reserve-tab">ご予約・お問い合わせ</div>

<!-- hero -->
<div class="ph" role="img" aria-label="緑の芝生と木々に囲まれたキャンプ場の休憩小屋と青空" style="left:0;top:0;width:1200px;height:390px;background:linear-gradient(180deg,#8ec3ea 0%,#cfe6f5 30%,#6f9b4c 55%,#4d7a33 80%,#7fae4c 100%)"></div>
<h1 class="hero-title"><span>雄大な自然と動植物</span><br>癒やしの空間を体験</h1>
<div class="ph" role="img" aria-label="芝生の広場" style="left:0;top:360px;width:300px;height:110px;background:linear-gradient(#9dc46a,#5f8f3a)"></div>
<div class="ph" role="img" aria-label="川遊びをする子どもたち" style="left:300px;top:360px;width:300px;height:110px;background:linear-gradient(#a9c9d8,#6b8f6a)"></div>
<div class="ph" role="img" aria-label="バーベキューの食材が並ぶグリル" style="left:600px;top:360px;width:300px;height:110px;background:linear-gradient(#8a6b4f,#4e3a2a)"></div>
<div class="ph" role="img" aria-label="バーベキューを楽しむ家族" style="left:900px;top:360px;width:300px;height:110px;background:linear-gradient(#d9a38a,#7b8f5a)"></div>
<div class="ph" role="img" aria-label="葉の飾り" style="left:0;top:460px;width:1200px;height:80px;background:linear-gradient(180deg,rgba(140,193,82,.55),rgba(255,255,255,0))"></div>

<!-- concept -->
<div class="abs" style="left:0;top:660px;width:1200px;text-align:center"><h2 class="sec-title underline">かわべリゾートのこだわり</h2></div>
<p class="abs body-text" style="left:140px;top:720px;width:920px">
豊かな自然に囲まれたキャンプ場で、川のせせらぎや鳥のさえずりを感じながら、ゆったりとした時間をお過ごしいただけます。季節ごとに表情を変える景色の中で、家族や仲間と特別なひとときを楽しめます。<br>
広い芝生の広場やバーベキュー施設、川遊びができる水辺など、子どもから大人まで楽しめる設備を整えております。日常を離れ、自然の中でのびのびと過ごす体験をご用意しています。<br>
野生の動物や鳥たちが暮らす環境を大切にしながら、訪れる皆さまが安心して過ごせる場所づくりを心がけています。ぜひ一度、癒やしの空間を体験しにお越しください。
</p>

<!-- facility -->
<div class="ph" role="img" aria-label="キャンプ場の敷地案内イラストマップ" style="left:0;top:900px;width:810px;height:320px;background:linear-gradient(135deg,#9ccb6a,#5f9a3c 60%,#7fbf5a)"></div>
<div class="panel" style="left:810px;top:900px;width:390px;height:320px">
  <h3 class="card-title">施設紹介</h3>
  <p class="body-text">バーベキュー場や芝生広場、川遊びエリアなど多彩な施設をご用意しています。各エリアの詳しい内容や設備は、施設紹介ページでご確認いただけます。</p>
  <span class="more-btn"><svg viewBox="0 0 14 14"><circle cx="7" cy="7" r="6" fill="none" stroke="currentColor"/><path d="M6 4l3 3-3 3" fill="none" stroke="currentColor"/></svg>詳しくはこちら</span>
</div>

<!-- reservation -->
<div class="panel" style="left:0;top:1240px;width:390px;height:300px">
  <h3 class="card-title">予約の流れ</h3>
  <p class="body-text">ご利用日と人数をお決めいただき、お電話またはフォームからご予約ください。確認のご連絡をもって予約完了となります。</p>
  <span class="more-btn"><svg viewBox="0 0 14 14"><circle cx="7" cy="7" r="6" fill="none" stroke="currentColor"/><path d="M6 4l3 3-3 3" fill="none" stroke="currentColor"/></svg>詳しくはこちら</span>
</div>
<div class="ph" role="img" aria-label="屋根付きの炊事場でバーベキューを準備する人たち" style="left:390px;top:1240px;width:810px;height:300px;background:linear-gradient(135deg,#6e5a44,#a08a6a 45%,#5d7a44)"></div>

<!-- access -->
<div class="ph" role="img" aria-label="キャンプ場周辺の道路地図" style="left:0;top:1560px;width:870px;height:320px;background:linear-gradient(135deg,#eef0ea,#dfe6d8)"></div>
<svg class="abs" style="left:420px;top:1680px" width="26" height="36" viewBox="0 0 26 36"><path d="M13 35C13 35 2 20 2 13a11 11 0 0 1 22 0c0 7-11 22-11 22z" fill="#e2462f"/><circle cx="13" cy="13" r="4.5" fill="#fff"/></svg>
<div class="panel" style="left:870px;top:1560px;width:330px;height:320px">
  <h3 class="card-title">アクセス方法</h3>
  <p class="body-text">お車でお越しの場合は最寄りのインターから約二十分です。公共交通機関をご利用の場合は、駅から送迎バスをご利用いただけます。</p>
  <span class="more-btn"><svg viewBox="0 0 14 14"><circle cx="7" cy="7" r="6" fill="none" stroke="currentColor"/><path d="M6 4l3 3-3 3" fill="none" stroke="currentColor"/></svg>詳しくはこちら</span>
</div>

<!-- voices -->
<div class="abs" style="left:0;top:1905px;width:1200px"><h2 class="sec-title">お客様の声</h2></div>
<div class="voice" style="left:180px;top:2000px">
  <div class="ph" role="img" aria-label="芝生で遊ぶ家族" style="background:linear-gradient(#bcd59a,#6f9a47)"></div>
  <div class="voice-body"><h4>タイトルが入ります</h4><p class="body-text">子どもたちが川遊びに夢中でした。自然の中でゆっくり過ごせて、家族みんな大満足です。また来たいです。</p></div>
</div>
<div class="voice" style="left:620px;top:2000px">
  <div class="ph" role="img" aria-label="キャンプを楽しむ仲間たち" style="background:linear-gradient(#c9d8b0,#7a8f5a)"></div>
  <div class="voice-body"><h4>タイトルが入ります</h4><p class="body-text">設備がきれいで初めてでも安心でした。鳥の声を聞きながらのバーベキューは最高でした。</p></div>
</div>

<!-- faq -->
<div class="ph" role="img" aria-label="緑の水彩風の背景" style="left:0;top:2190px;width:1200px;height:380px;background:linear-gradient(180deg,#fff 0%,#9fd06a 14%,#5fae3a 60%,#79bf4c 100%)"></div>
<div class="abs" style="left:0;top:2230px;width:1200px"><h2 class="sec-title">よくある質問</h2></div>
<div class="faq-item" style="top:2300px">
  <span class="q">Q</span>
  <h4>ここに質問が入ります。ここに質問が入ります。ここに質問が入ります。</h4>
  <p class="body-text">回答が入ります。ご利用に関するよくあるご質問への回答をこちらに掲載いたします。ご不明な点はお気軽にお問い合わせください。</p>
</div>
<div class="faq-item" style="top:2430px">
  <span class="q">Q</span>
  <h4>ここに質問が入ります。ここに質問が入ります。ここに質問が入ります。</h4>
  <p class="body-text">回答が入ります。ご利用に関するよくあるご質問への回答をこちらに掲載いたします。ご不明な点はお気軽にお問い合わせください。</p>
</div>

<!-- recruit -->
<div class="abs" style="left:0;top:2570px;width:1200px;height:420px;background:var(--blue)"></div>
<div class="abs" style="left:210px;top:2600px;width:780px;height:340px;background:#fff;padding:40px 50px;text-align:center">
  <h2 class="sec-title" style="margin-bottom:16px">採用情報</h2>
  <p class="body-text" style="text-align:left">自然が好きな方、人と接することが好きな方を募集しています。キャンプ場の運営スタッフとして、受付や施設管理、イベントの企画などをお任せします。未経験の方も丁寧にサポートいたしますので安心してご応募ください。私たちと一緒に、訪れる皆さまに癒やしの時間を届けませんか。</p>
  <span class="more-btn"><svg viewBox="0 0 14 14"><circle cx="7" cy="7" r="6" fill="none" stroke="currentColor"/><path d="M6 4l3 3-3 3" fill="none" stroke="currentColor"/></svg>詳しくはこちら</span>
</div>
<div class="ph" role="img" aria-label="ジャンプする若者たち" style="left:1010px;top:2800px;width:170px;height:160px;background:linear-gradient(#4a9fe0,#2d78b5)"></div>
<div class="ph" role="img" aria-label="芝生の縁取り" style="left:0;top:2975px;width:1200px;height:55px;background:linear-gradient(180deg,#8cc152,#5a9e2f)"></div>

<!-- footer -->
<footer class="site-footer">
  <div class="brand" style="justify-content:center;font-size:22px;margin-top:28px"><i></i>かわべリゾート</div>
  <p style="font-size:12px;margin-top:6px">〒000-0000 〇〇県〇〇市〇〇町0-0<br>受付時間 9:00〜17:00</p>
  <span class="tel-btn">お問い合わせ 0120-345-678</span>
  <nav class="fnav" style="margin-top:26px"><span>HOME</span><span>施設紹介</span><span>予約の流れ</span><span>よくある質問</span><span>お客様の声</span><span>アクセス</span><span>採用情報</span></nav>
  <p class="copy">Copyright © かわべリゾート All Rights Reserved.</p>
</footer>

</body>
</html>
```